Application Dashboard Skin - Non coded theme only

We are looking for a website color theme/look feel for a new .net dashboard application we are building. Target audience who will be using this are E and C level professionals. We are looking for the following:

Images of optional color themes for our existing dashboard. You can access a temporary version with no styling here: http://demo.plexaroni-app.com:99/ . Application built in telerik and highcharts.

We are not looking for finished code or application skins. Our development team will take your final design (with specific colors/images/etc. provided) and apply it to the final beta version of the application.

Design considerations:
We are open to creative ideas, but please know that preference will be given to professional designs with emphasis on a consistent brand look/feel. Designs and colors should be focused on quickly identifying and processing the data.

Multiple submissions welcome.

-Quorventa team

Target Market(s)

IT / Insurance

Industry/Entity Type

Building

Number of Pages Required

3 page

Requirements
Must have
• Application Dashboard link for design: http://demo.plexaroni-app.com:99/

```html
<!DOCTYPE html>
<html lang="en">
<head>
<meta charset="utf-8">
<title>Claimvista — Accuracy Results</title>
<link href="https://fonts.googleapis.com/css2?family=Open+Sans:wght@400;600;700&display=swap" rel="stylesheet">
<style>
  :root{
    --orange:#f7941d;
    --orange-light:#fba73f;
    --slate:#5d6573;
    --slate-light:#6e7685;
    --ink:#4a4f5a;
    --muted:#6b6f78;
    --page:#ececee;
    --panel:#ffffff;
    --stripe:#efeff1;
    --grid:#e2e3e6;
  }
  *{box-sizing:border-box;margin:0;padding:0}
  html,body{width:1021px;height:1200px;overflow:hidden}
  body{position:relative;background:var(--page);font-family:"Open Sans",Arial,sans-serif;color:var(--ink)}
  .abs{position:absolute}

  /* header */
  .brand-bar{left:0;top:0;width:1021px;height:60px;background:#fff;border-bottom:1px solid #dcdde0}
  .brand{left:26px;top:17px;display:flex;align-items:center;gap:6px;font-size:19px;font-weight:400;color:#333}
  .brand-dot{width:12px;height:12px;border-radius:50%;background:var(--orange)}
  .main-nav{left:202px;top:11px;width:808px;height:38px;background:var(--slate);display:flex}
  .nav-tab{height:38px;display:flex;align-items:center;justify-content:center;color:#fff;font-size:10px;font-weight:700;position:relative;border-right:1px solid #6c7482}
  .nav-tab.active{background:var(--orange)}
  .nav-tab.active::after{content:"";position:absolute;bottom:-5px;left:50%;margin-left:-5px;border:5px solid transparent;border-bottom:0;border-top-color:var(--orange)}
  .gear{left:980px;top:20px}

  /* panels */
  .panel{background:var(--panel);box-shadow:0 1px 2px rgba(0,0,0,.08)}
  .panel-title{font-size:13px;font-weight:600;color:var(--ink)}
  .hint{font-size:10px;font-weight:600;color:var(--orange)}
  .select{height:23px;display:flex;align-items:center;justify-content:space-between;padding:0 9px 0 11px;font-size:10px}
  .select.light{background:#f0f0f2;color:#aaa}
  .select.dark{background:var(--slate-light);color:#9aa0ab}
  .select.warm{background:#f9a843;color:#fde3c2}
  .caret{border:5px solid transparent;border-bottom:0;border-top-color:currentColor}
  .menu{width:14px;height:12px;display:flex;flex-direction:column;justify-content:space-between}
  .menu span{height:2.4px;background:#4f5663;border-radius:1px}

  .impact-band{left:11px;top:398px;width:705px;height:46px;background:var(--slate);display:flex;align-items:center;padding-left:19px;color:#fff;font-size:13px;font-weight:600;gap:10px}
  .filter-tabs{left:11px;top:450px;width:705px;height:28px;background:var(--orange-light);display:flex}
  .filter-tab{width:105px;display:flex;align-items:center;justify-content:center;font-size:10px;color:#fff}
  .filter-tab.current{background:#fff;color:var(--ink);font-weight:600}
  .filter-tab.strong{background:var(--orange)}

  .section-head{display:flex;align-items:center;gap:14px;font-size:12.5px;font-weight:600;color:var(--orange)}
  .section-head .scope{font-size:10px;font-weight:400;color:var(--ink);border-left:1px solid #ccc;padding-left:12px}
  .row-labels div{height:27px;line-height:27px;padding-left:14px;font-size:10px;color:#555;white-space:nowrap}
  .row-labels div:nth-child(odd){background:var(--stripe)}
  .axis-name{font-size:10.5px;font-weight:700;color:var(--ink)}

  /* KPIs */
  .kpi-head{left:726px;top:70px;width:284px;height:42px;background:var(--orange);display:flex;align-items:center;padding:0 10px 0 13px;color:#fff;font-weight:700;font-size:12px;gap:10px}
  .kpi-total{left:726px;top:112px;width:284px;height:35px;background:var(--slate);color:#fff;font-size:9.5px;font-weight:700;display:flex;align-items:center;justify-content:center}
  .kpi-list{left:726px;top:147px;width:284px;background:#fff}
  .kpi-row{height:30.3px;display:flex;align-items:center;font-size:9.5px;color:#555}
  .kpi-row:nth-child(even){background:var(--stripe)}
  .kpi-row .k{width:195px;padding-left:12px}
  .kpi-row .v{font-weight:700;color:var(--ink)}
  .ratio-panel{left:726px;width:284px;background:#fff;border-top:1px solid #e3e3e6}
</style>
</head>
<body>

<header>
  <div class="abs brand-bar"></div>
  <div class="abs brand"><span>Claimvista</span><span class="brand-dot"></span></div>
  <nav class="abs main-nav">
    <div class="nav-tab active" style="width:138px">Accuracy Results</div>
    <div class="nav-tab" style="width:140px">Processor Accuracy</div>
    <div class="nav-tab" style="width:138px">Manage Users</div>
  </nav>
  <svg class="abs gear" width="18" height="18" viewBox="0 0 24 24" aria-label="Settings">
    <path fill="#fff" d="M19.4 13a7.5 7.5 0 0 0 0-2l2.1-1.6-2-3.5-2.5 1a7.6 7.6 0 0 0-1.7-1L15 3h-4l-.4 2.7a7.6 7.6 0 0 0-1.7 1l-2.5-1-2 3.5L4.6 11a7.5 7.5 0 0 0 0 2l-2.1 1.6 2 3.5 2.5-1a7.6 7.6 0 0 0 1.7 1L11 21h4l.4-2.7a7.6 7.6 0 0 0 1.7-1l2.5 1 2-3.5zM13 15.5a3.5 3.5 0 1 1 0-7 3.5 3.5 0 0 1 0 7z" transform="translate(-1 0)"/>
  </svg>
</header>

<!-- YTD accuracy -->
<section class="abs panel" style="left:11px;top:70px;width:705px;height:317px">
  <div class="abs" style="left:14px;top:16px;display:flex;align-items:center;gap:8px">
    <svg width="18" height="18" viewBox="0 0 18 18"><circle cx="9" cy="9" r="7.5" fill="none" stroke="#5d6573" stroke-width="1.4"/><circle cx="9" cy="9" r="4.5" fill="none" stroke="#5d6573" stroke-width="1.4"/><circle cx="9" cy="9" r="1.6" fill="#5d6573"/></svg>
    <span class="panel-title">YTD overall accuracy Results</span>
    <span style="width:1px;height:14px;background:#ccc;margin:0 7px"></span>
    <span class="hint">Click the bars to view YTD details for the specific region</span>
  </div>
  <div class="abs select light" style="left:531px;top:12px;width:126px"><span>End to End</span><span class="caret"></span></div>
  <div class="abs menu" style="left:674px;top:18px"><span></span><span></span><span></span></div>
</section>
<svg class="abs" style="left:11px;top:118px" width="705" height="269" viewBox="14 148 881 336" aria-label="YTD accuracy by region">
  <g stroke="var(--grid)" stroke-width="1">
    <line x1="32" y1="193" x2="875" y2="193"/><line x1="32" y1="240" x2="875" y2="240"/>
    <line x1="32" y1="287" x2="875" y2="287"/><line x1="32" y1="334" x2="875" y2="334"/>
    <line x1="32" y1="381" x2="875" y2="381"/><line x1="32" y1="428" x2="875" y2="428"/>
    <line x1="32" y1="148" x2="32" y2="428"/><line x1="73" y1="148" x2="73" y2="428"/>
    <line x1="225" y1="148" x2="225" y2="428"/><line x1="385" y1="148" x2="385" y2="428"/>
    <line x1="546" y1="148" x2="546" y2="428"/><line x1="707" y1="148" x2="707" y2="428"/>
    <line x1="875" y1="148" x2="875" y2="428"/>
  </g>
  <g font-size="12" fill="#555" font-family="Open Sans, sans-serif">
    <text x="42" y="174">100</text><text x="42" y="221">97.5</text><text x="42" y="268">95</text>
    <text x="42" y="315">92.5</text><text x="42" y="362">90</text><text x="42" y="411">87.5</text>
  </g>
  <g fill="var(--orange)">
    <rect x="121" y="222" width="55" height="206"/><rect x="276" y="210" width="55" height="218"/>
    <rect x="439" y="250" width="55" height="178"/><rect x="601" y="222" width="55" height="206"/>
    <rect x="762" y="222" width="55" height="206"/>
  </g>
  <g fill="#fff" font-size="11.5" font-weight="700" text-anchor="middle" font-family="Open Sans, sans-serif">
    <text x="148" y="243">97.7%</text><text x="303" y="231">98.5%</text><text x="466" y="273">96.8%</text>
    <text x="628" y="243">97.7%</text><text x="789" y="243">94.9%</text>
  </g>
  <g fill="var(--ink)" font-size="12.5" font-weight="700" text-anchor="middle" font-family="Open Sans, sans-serif">
    <text x="147" y="462">Colorado</text><text x="303" y="462">Georgia</text><text x="467" y="462">Hawaii</text>
    <text x="632" y="462">Midatlantic</text><text x="790" y="462">Northwest</text>
  </g>
</svg>

<!-- Error impact -->
<div class="abs impact-band">
  <svg width="18" height="16" viewBox="0 0 18 16"><path d="M9 1.2 17 15H1z" fill="none" stroke="#fff" stroke-width="1.4" stroke-linejoin="round"/><line x1="9" y1="6" x2="9" y2="10.5" stroke="#fff" stroke-width="1.5"/><circle cx="9" cy="12.6" r=".9" fill="#fff"/></svg>
  <span>Error impact for june 2016</span>
</div>
<div class="abs select dark" style="left:575px;top:410px;width:126px"><span>All Regions</span><span class="caret"></span></div>
<div class="abs filter-tabs">
  <div class="filter-tab current">All Errors</div>
  <div class="filter-tab strong">Providers</div>
  <div class="filter-tab">Employers</div>
  <div class="filter-tab strong">Line Of Business</div>
</div>

<!-- Top 10 by count -->
<section class="abs panel" style="left:11px;top:485px;width:705px;height:344px">
  <div class="abs section-head" style="left:14px;top:11px"><span>Top 10 Error Reasons</span><span class="scope">All Regions</span></div>
  <div class="abs menu" style="left:677px;top:14px"><span></span><span></span><span></span></div>
  <div class="abs" style="left:0;top:40px;width:705px;height:1px;background:#e3e3e6"></div>
  <div class="abs row-labels" style="left:0;top:41px;width:191px">
    <div>Incorrect Contract ...</div><div>Claim Paid Incorrectly</div><div>Not A Halvern Benefit.  Bill...</div>
    <div>Incorrect Co-Pay / C...</div><div>Copay Amount Not Correct</div><div>Did Not Follow Desk ...</div>
    <div>Did Not Follow Pnp</div><div>Claim Denied In Error...</div><div>Unknown</div><div>Denied Incorrectly -...</div>
  </div>
  <div class="abs axis-name" style="left:12px;top:319px">COUNT</div>
</section>
<svg class="abs" style="left:202px;top:526px" width="514" height="303" viewBox="252 657 643 379" aria-label="Top 10 error reasons by count">
  <g stroke="var(--grid)"><line x1="403" y1="657" x2="403" y2="995"/><line x1="553" y1="657" x2="553" y2="995"/><line x1="703" y1="657" x2="703" y2="995"/><line x1="853" y1="657" x2="853" y2="995"/><line x1="252" y1="995" x2="853" y2="995"/></g>
  <g stroke="var(--orange)" stroke-width="2.5">
    <line x1="253" y1="673" x2="781" y2="673"/><line x1="253" y1="707" x2="655" y2="707"/>
    <line x1="253" y1="740" x2="617" y2="740"/><line x1="253" y1="774" x2="590" y2="774"/>
    <line x1="253" y1="807" x2="560" y2="807"/><line x1="253" y1="841" x2="564" y2="841"/>
    <line x1="253" y1="876" x2="533" y2="876"/><line x1="253" y1="908" x2="474" y2="908"/>
    <line x1="253" y1="941" x2="474" y2="941"/><line x1="253" y1="975" x2="437" y2="975"/>
  </g>
  <g fill="var(--slate)">
    <circle cx="781" cy="673" r="10"/><circle cx="655" cy="707" r="10"/><circle cx="617" cy="740" r="10"/>
    <circle cx="590" cy="774" r="10"/><circle cx="560" cy="807" r="10"/><circle cx="564" cy="841" r="10"/>
    <circle cx="533" cy="876" r="10"/><circle cx="474" cy="908" r="10"/><circle cx="474" cy="941" r="10"/>
    <circle cx="437" cy="975" r="10"/>
  </g>
  <g fill="#fff" font-size="10" font-weight="700" text-anchor="middle" font-family="Open Sans, sans-serif">
    <text x="781" y="677">35</text><text x="655" y="711">26</text><text x="617" y="744">24</text>
    <text x="590" y="778">23</text><text x="560" y="811">20</text><text x="564" y="845">20</text>
    <text x="533" y="880">19</text><text x="474" y="912">14</text><text x="474" y="945">14</text>
    <text x="437" y="979">12</text>
  </g>
  <g fill="var(--ink)" font-size="12" font-weight="600" text-anchor="middle" font-family="Open Sans, sans-serif">
    <text x="255" y="1019">0</text><text x="402" y="1019">10</text><text x="554" y="1019">20</text>
    <text x="704" y="1019">30</text><text x="849" y="1019">40</text>
  </g>
</svg>

<!-- Top 10 financial impact -->
<section class="abs panel" style="left:11px;top:841px;width:705px;height:346px">
  <div class="abs section-head" style="left:14px;top:11px"><span>Top 10 Error Reasons - Financial Impact</span><span class="scope">All Regions</span></div>
  <div class="abs menu" style="left:677px;top:14px"><span></span><span></span><span></span></div>
  <div class="abs" style="left:0;top:41px;width:705px;height:1px;background:#e3e3e6"></div>
  <div class="abs row-labels" style="left:0;top:42px;width:191px">
    <div>Incorrect Contract ...</div><div>Claim Paid Incorrectly</div><div>Not A Halvern Benefit.  Bill...</div>
    <div>Incorrect Co-Pay / C...</div><div>Copay Amount Not Correct</div><div>Did Not Follow Desk ...</div>
    <div>Did Not Follow Pnp</div><div>Claim Denied In Error...</div><div>Unknown</div><div>Denied Incorrectly -...</div>
  </div>
  <div class="abs axis-name" style="left:12px;top:322px">$ Amount</div>
</section>
<svg class="abs" style="left:202px;top:883px" width="514" height="303" viewBox="252 1104 643 379" aria-label="Top 10 error reasons by financial impact">
  <g stroke="var(--grid)"><line x1="372" y1="1104" x2="372" y2="1442"/><line x1="492" y1="1104" x2="492" y2="1442"/><line x1="613" y1="1104" x2="613" y2="1442"/><line x1="733" y1="1104" x2="733" y2="1442"/><line x1="853" y1="1104" x2="853" y2="1442"/><line x1="252" y1="1442" x2="853" y2="1442"/></g>
  <g stroke="var(--orange)" stroke-width="2.5">
    <line x1="458" y1="1121" x2="772" y2="1121"/><line x1="589" y1="1155" x2="757" y2="1155"/>
    <line x1="716" y1="1189" x2="734" y2="1189"/><line x1="722" y1="1220" x2="757" y2="1220"/>
    <line x1="704" y1="1254" x2="747" y2="1254"/><line x1="722" y1="1288" x2="747" y2="1288"/>
    <line x1="589" y1="1323" x2="757" y2="1323"/><line x1="722" y1="1358" x2="767" y2="1358"/>
    <line x1="722" y1="1393" x2="747" y2="1393"/><line x1="722" y1="1426" x2="747" y2="1426"/>
  </g>
  <g fill="var(--slate)">
    <rect x="386" y="1111" width="74" height="20" rx="10"/><rect x="771" y="1111" width="70" height="20" rx="10"/>
    <rect x="517" y="1145" width="74" height="20" rx="10"/><rect x="756" y="1145" width="62" height="20" rx="10"/>
    <rect x="670" y="1179" width="46" height="20" rx="10"/>
    <rect x="690" y="1210" width="32" height="20" rx="10"/><rect x="756" y="1210" width="57" height="20" rx="10"/>
    <rect x="659" y="1244" width="46" height="20" rx="10"/><rect x="746" y="1244" width="38" height="20" rx="10"/>
    <rect x="690" y="1278" width="32" height="20" rx="10"/><rect x="746" y="1278" width="32" height="20" rx="10"/>
    <rect x="517" y="1313" width="74" height="20" rx="10"/><rect x="756" y="1313" width="69" height="20" rx="10"/>
    <rect x="690" y="1348" width="32" height="20" rx="10"/><rect x="766" y="1348" width="57" height="20" rx="10"/>
    <rect x="690" y="1383" width="32" height="20" rx="10"/><rect x="746" y="1383" width="50" height="20" rx="10"/>
    <rect x="690" y="1416" width="32" height="20" rx="10"/><rect x="746" y="1416" width="66" height="20" rx="10"/>
  </g>
  <g fill="#fff" font-size="10" font-weight="700" text-anchor="middle" font-family="Open Sans, sans-serif">
    <text x="423" y="1125">$ -65155.67</text><text x="806" y="1125">$ 12510.63</text>
    <text x="554" y="1159">$ -26915.92</text><text x="787" y="1159">$ 2919.39</text>
    <text x="693" y="1193">$ -245</text>
    <text x="706" y="1224">$ 0</text><text x="784" y="1224">$ 693.01</text>
    <text x="682" y="1258">$ -295</text><text x="765" y="1258">$ 10</text>
    <text x="706" y="1292">$ 0</text><text x="762" y="1292">$ 0</text>
    <text x="554" y="1327">$ -29341.33</text><text x="790" y="1327">$ 10390.26</text>
    <text x="706" y="1362">$ 0</text><text x="794" y="1362">$ 6509.7</text>
    <text x="706" y="1397">$ 0</text><text x="771" y="1397">$ 331.1</text>
    <text x="706" y="1430">$ 0</text><text x="779" y="1430">$ 1805.56</text>
  </g>
  <g fill="var(--ink)" font-size="12" font-weight="600" text-anchor="middle" font-family="Open Sans, sans-serif">
    <text x="254" y="1467">-80k</text><text x="372" y="1467">-60k</text><text x="491" y="1467">-40k</text>
    <text x="612" y="1467">-20k</text><text x="732" y="1467">0k</text><text x="845" y="1467">20k</text>
  </g>
</svg>

<!-- KPIs -->
<div class="abs kpi-head">
  <svg width="20" height="20" viewBox="0 0 20 20"><circle cx="10" cy="10" r="8.5" fill="none" stroke="#fff" stroke-width="1.5"/><path d="M6 10.2 8.8 13 14 7.5" fill="none" stroke="#fff" stroke-width="1.6"/></svg>
  <span style="flex:1">KPI's</span>
  <div class="select warm" style="width:125px"><span>All Regions</span><span class="caret"></span></div>
</div>
<div class="abs kpi-total">Overall YTD Accuracy 97.41%</div>
<div class="abs kpi-list">
  <div class="kpi-row"><span class="k">Claims Audited:</span><span class="v">4859</span></div>
  <div class="kpi-row"><span class="k">Avg. Claims Audited per day:</span><span class="v">6.7</span></div>
  <div class="kpi-row"><span class="k">Errors Found:</span><span class="v">2147</span></div>
  <div class="kpi-row"><span class="k">Financial Impact:</span><span class="v">$1,462,139</span></div>
  <div class="kpi-row"><span class="k">Total Claims Posted:</span><span class="v">17,773,591</span></div>
  <div class="kpi-row"><span class="k">Total Encounter Claims:</span><span class="v">93,984,586</span></div>
  <div class="kpi-row"><span class="k">Total Auto Adjudication Claim Count:</span><span class="v">920,918</span></div>
  <div class="kpi-row"><span class="k">Total Adjustment Claim Count:</span><span class="v">920,918</span></div>
  <div class="kpi-row"><span class="k">Total Denied Claim Count:</span><span class="v">133,523</span></div>
  <div class="kpi-row"><span class="k">Total Dollars Paid:</span><span class="v">$5,669,835,044</span></div>
  <div class="kpi-row"><span class="k">Auto Adjudication Rate:</span><span class="v">$0.052</span></div>
  <div class="kpi-row"><span class="k">Adjustment Rate:</span><span class="v">1.345%</span></div>
  <div class="kpi-row"><span class="k">Denial Rate:</span><span class="v">0.751%</span></div>
</div>

<!-- Paid vs Denied -->
<section class="abs ratio-panel" style="top:550px;height:258px"></section>
<svg class="abs" style="left:726px;top:550px" width="284" height="258" viewBox="908 688 354 322" aria-label="Paid versus denied">
  <g fill="#4f5663"><rect x="1234" y="716" width="17" height="3" rx="1"/><rect x="1234" y="722" width="17" height="3" rx="1"/><rect x="1234" y="728" width="17" height="3" rx="1"/></g>
  <circle cx="1080" cy="852" r="107" fill="none" stroke="var(--orange)" stroke-width="3"/>
  <circle cx="1080" cy="852" r="107" fill="none" stroke="var(--slate)" stroke-width="3" stroke-dasharray="47 625" transform="rotate(-90 1080 852)"/>
  <g font-family="Open Sans, sans-serif" text-anchor="middle">
    <text x="1080" y="827" font-size="23" font-weight="700" fill="var(--ink)">Paid</text>
    <circle cx="1080" cy="852" r="13" fill="var(--orange)"/>
    <text x="1080" y="857" font-size="12" font-weight="700" fill="var(--slate)">vs</text>
    <text x="1080" y="893" font-size="23" font-weight="700" fill="var(--ink)">Denied</text>
    <circle cx="1016" cy="765" r="26" fill="var(--orange)"/>
    <text x="1016" y="762" font-size="12.5" font-weight="700" fill="#fff">Paid</text>
    <text x="1016" y="775" font-size="10" font-weight="700" fill="#fff">99.3%</text>
    <circle cx="1146" cy="940" r="26" fill="var(--slate)"/>
    <text x="1146" y="938" font-size="11.5" font-weight="700" fill="#fff">Denied</text>
    <text x="1146" y="951" font-size="10" font-weight="700" fill="#fff">0.7%</text>
  </g>
</svg>

<!-- Paid vs Encounter -->
<section class="abs ratio-panel" style="top:810px;height:283px"></section>
<svg class="abs" style="left:726px;top:810px" width="284" height="282" viewBox="908 1012 354 353" aria-label="Paid versus encounter">
  <g fill="#4f5663"><rect x="1234" y="1040" width="17" height="3" rx="1"/><rect x="1234" y="1046" width="17" height="3" rx="1"/><rect x="1234" y="1052" width="17" height="3" rx="1"/></g>
  <circle cx="1080" cy="1185" r="107" fill="none" stroke="var(--orange)" stroke-width="3"/>
  <circle cx="1080" cy="1185" r="107" fill="none" stroke="var(--slate)" stroke-width="3" stroke-dasharray="222 450" transform="rotate(175 1080 1185)"/>
  <g font-family="Open Sans, sans-serif" text-anchor="middle">
    <text x="1080" y="1159" font-size="23" font-weight="700" fill="var(--ink)">Paid</text>
    <circle cx="1080" cy="1185" r="13" fill="var(--orange)"/>
    <text x="1080" y="1190" font-size="12" font-weight="700" fill="var(--slate)">vs</text>
    <text x="1080" y="1226" font-size="23" font-weight="700" fill="var(--ink)">Encounter</text>
    <circle cx="1016" cy="1097" r="26" fill="var(--slate)"/>
    <text x="1016" y="1094" font-size="12.5" font-weight="700" fill="#fff">Paid</text>
    <text x="1016" y="1107" font-size="10" font-weight="700" fill="#fff">15.9%</text>
    <circle cx="1146" cy="1272" r="26" fill="var(--orange)"/>
    <text x="1146" y="1270" font-size="11.5" font-weight="700" fill="#fff">Denied</text>
    <text x="1146" y="1283" font-size="10" font-weight="700" fill="#fff">84.1%</text>
  </g>
</svg>

</body>
</html>
```